Eco conscious print and frame company needs a website

‘VURleaf is a new company that makes frames and fine art prints from sustainable bamboo. Our site should have an organic feel yet still have a professional clean look to it as well.
We need shopping cart and image uploading capabilities much like a pixelbarn or photomoth type of site only on a much smaller scale.
Currently we have 3 different styles available in sizes from 8"x8" all the way to 4ft by 8ft.
Target audience will be the lumograffic, picturely, zaphone market.

Target Market(s)

20-40 years old male and female. Picturely generation.

Industry/Entity Type

Shopping

Requirements
Must have
• Front end and back end capabilities with emphasis on image uploading and shopping cart functionality.

```html
<!DOCTYPE html>
<html lang="en">
<head>
<meta charset="utf-8">
<title>VURleaf Frame Company</title>
<link href="https://fonts.googleapis.com/css2?family=Open+Sans:wght@400;600;700&family=Oswald:wght@300;400;500&display=swap" rel="stylesheet">
<style>
:root{
  --page:#ebebeb;
  --panel-edge:#ffffff;
  --ink:#2f2f2f;
  --ink-soft:#4a4a4a;
  --green:#5b9a24;
  --green-dark:#3f7d12;
  --green-text:#5a9a2a;
  --wood-light:#f3cf8f;
  --wood:#ebbd72;
  --wood-dark:#e0ad5e;
  --tab-light:rgba(255,248,235,.45);
  --grey-arrow:#b9b9b9;
}
*{margin:0;padding:0;box-sizing:border-box}
html,body{width:1200px;height:1200px;overflow:hidden;background:var(--page)}
body{position:relative;font-family:"Open Sans",sans-serif;color:var(--ink)}
.abs{position:absolute}

.header{left:108px;top:4px;width:980px;height:202px;border-radius:16px;background:var(--panel-edge);box-shadow:0 3px 6px rgba(0,0,0,.12)}
.header-inner{position:absolute;inset:7px;border-radius:12px;background:radial-gradient(ellipse at 50% 45%,#ffffff 0%,#f4f4f4 45%,#e3e3e3 100%)}
.main-menu{list-style:none;left:154px;top:35px}
.main-menu li{font-size:14px;letter-spacing:1.6px;height:24px;line-height:20px;color:var(--ink)}
.main-menu li.active{position:relative;font-weight:700}
.main-menu li.active::before{content:"";position:absolute;left:-8px;top:-1px;width:127px;height:22px;border-radius:3px;background:var(--green);z-index:-1}
.main-menu li.active span{position:relative}

.brand{left:470px;top:112px;width:256px;text-align:center}
.brand-name{font-size:44px;font-weight:400;color:var(--ink);line-height:52px;letter-spacing:-1px}

.account-links{right:142px;top:35px;font-size:12px;letter-spacing:1.4px;color:var(--ink)}
.search{left:830px;top:122px;width:226px;height:40px;background:#fff;border:1px solid #cfcfcf;box-shadow:0 4px 8px rgba(0,0,0,.1)}
.search-divider{position:absolute;left:182px;top:6px;width:1px;height:28px;background:#d8d8d8}
.search svg{position:absolute;left:190px;top:8px}

.offer-bar{top:228px;left:144px;width:912px;display:flex;justify-content:space-between;font-size:14px;letter-spacing:1.4px;color:var(--ink-soft)}
.offer-bar em{font-style:normal;color:var(--green-text)}

.hero{left:108px;top:262px;width:980px;height:488px;border-radius:16px;background:var(--panel-edge);box-shadow:0 3px 6px rgba(0,0,0,.12)}
.wood{background:linear-gradient(100deg,var(--wood-light) 0%,var(--wood) 35%,var(--wood-light) 60%,var(--wood-dark) 100%)}
.hero-inner{position:absolute;left:6px;top:7px;width:967px;height:474px;border-radius:11px;overflow:hidden}

.tab{left:0;width:247px;height:78px;padding:16px 0 0 19px;background:var(--tab-light)}
.tab h3{font-weight:400;font-size:25px;letter-spacing:2.3px;line-height:30px;color:var(--ink)}
.tab p{font-size:12px;letter-spacing:1.3px;color:var(--ink-soft)}
.tab.current{background:var(--green)}
.tab.current p{color:var(--ink)}
.tab.current::after{content:"";position:absolute;right:-30px;top:20px;border-left:30px solid var(--green-dark);border-top:20px solid transparent;border-bottom:20px solid transparent}

.shop-btn{left:0;top:364px;width:247px;height:78px;background:var(--green)}
.shop-btn svg{position:absolute;left:20px;top:16px}
.shop-btn span{position:absolute;left:115px;top:18px;font-family:"Oswald",sans-serif;font-size:28px;letter-spacing:2px;color:#fff}

.frame{left:320px;top:50px;width:370px;height:370px;transform:rotate(8deg);background:linear-gradient(135deg,#f6dfb6,#e8c48a);box-shadow:6px 10px 16px rgba(0,0,0,.25)}
.frame-photo{position:absolute;left:30px;top:30px;width:310px;height:310px;background:linear-gradient(180deg,#6f7b68 0%,#556a3e 45%,#3e5a24 75%,#b69a45 100%);border:4px solid #3b2b1c}

.hero-copy{left:734px;top:60px;width:192px;font-size:12px;line-height:18px;letter-spacing:.6px;color:var(--ink-soft)}
.hero-copy h2{font-weight:400;font-size:24px;letter-spacing:2.6px;color:var(--ink);line-height:30px;white-space:nowrap}
.hero-copy .kicker{margin:10px 0 15px;letter-spacing:1.2px;color:var(--ink)}
.hero-copy strong{color:var(--ink);font-weight:700}
.hero-copy strong.green{color:#2e5a0a}
.hero-copy p+p{margin-top:18px}
.more{left:825px;top:418px;font-size:12px;color:var(--green-dark);letter-spacing:1.2px}

.step-label{font-family:"Oswald",sans-serif;font-weight:400;font-size:20px;letter-spacing:1.5px;color:var(--ink);top:815px}
.step-num{width:81px;height:81px;border-radius:50%;background:var(--green);top:792px;color:#fff;font-family:"Oswald",sans-serif;font-size:38px;text-align:center;line-height:81px}
.step-cta{left:876px;top:811px;width:131px;height:39px;border:1px solid var(--green-dark);border-radius:2px;background:linear-gradient(#8fcf4e,#5ea52a);font-family:"Oswald",sans-serif;font-size:20px;letter-spacing:1.5px;color:#2c4d12;text-align:center;line-height:36px}

.feature{top:964px;width:280px}
.feature h4{font-family:"Oswald",sans-serif;font-weight:500;font-size:25px;color:var(--green-text);line-height:38px;letter-spacing:-.5px}
.feature p{font-size:16.5px;line-height:21.5px;color:var(--ink)}

.footer{left:108px;top:1100px;width:980px;height:120px;border-radius:16px;background:var(--panel-edge)}
.footer-inner{position:absolute;left:6px;top:7px;width:967px;height:120px;border-radius:11px}
.footer-links{left:137px;top:1131px;font-size:12px;letter-spacing:1.3px;color:var(--ink)}
.footer-links span{margin:0 11px}
.copyright{left:137px;top:1167px;font-size:12px;letter-spacing:1.3px;color:var(--ink)}
.social{top:1145px;width:28px;height:28px;border-radius:4px}
</style>
</head>
<body>

<header class="abs header"><div class="header-inner"></div></header>
<ul class="abs main-menu">
  <li>LOREM IPSUM MENU</li>
  <li>LOREM MENU</li>
  <li>LOREM IPSUM MENU</li>
  <li class="active"><span>LOREM MENU</span></li>
  <li>IPSUM MENU</li>
  <li>MENU</li>
</ul>
<div class="abs brand">
  <div class="brand-name">VURleaf</div>
</div>
<div class="abs account-links">SIGN IN | SIGN UP | HELP |</div>
<div class="abs search">
  <div class="search-divider"></div>
  <svg width="30" height="26" viewBox="0 0 30 26"><circle cx="10" cy="10" r="7.5" fill="none" stroke="#333" stroke-width="3"/><line x1="15.5" y1="15.5" x2="25" y2="23" stroke="#333" stroke-width="4.5" stroke-linecap="round"/></svg>
</div>

<div class="abs offer-bar">
  <div>LIMITED TIME OFFER LOREM IPSUM SALE <em>SAVE UP TO 50%</em></div>
  <div><em>FREE SHIPPING</em> ON ORDERS $30+, ENTER CODE: SHIP30</div>
</div>

<section class="abs hero">
  <div class="hero-inner wood">
    <div class="abs tab" style="top:33px"><h3>LOREM IPSUM</h3><p>LOREM IPSUM DOLOR</p></div>
    <div class="abs tab current" style="top:112px"><h3>LOREM IPSUM</h3><p>LOREM IPSUM DOLOR</p></div>
    <div class="abs tab" style="top:191px"><h3>LOREM IPSUM</h3><p>LOREM IPSUM DOLOR</p></div>
    <div class="abs shop-btn">
      <svg width="48" height="48" viewBox="0 0 48 48"><polygon points="2,0 46,24 2,48" fill="#fff"/></svg>
      <span>SHOP</span>
    </div>
    <div class="abs frame">
      <div class="frame-photo" role="img" aria-label="Framed photo of a child standing on a boat among tropical palms"></div>
    </div>
    <div class="abs hero-copy">
      <h2>LOREM IPSUM</h2>
      <div class="kicker">LOREM IPSUM</div>
      <p><strong>This is Layercraft's version of Lorem Ipsum</strong>. Proin gravida nibh vel velit auctor aliquet. Aenean sollicitudin, lorem quis bibendum auctor, nisi elit consequat ipsum, nec sagittis sem nibh id elit.</p>
      <p><strong class="green">Duis sed odio sit amet nibh vulputate cursus a sit amet mauris</strong>. Morbi accumsan ipsum velit. Nam nec tellus a odio tincidunt auctor a ornare odio. Sed</p>
    </div>
    <div class="abs more">LOREM IPSUM &gt;&gt;</div>
  </div>
</section>

<div class="abs step-label" style="left:166px">Lorem ipsum</div>
<div class="abs step-num" style="left:292px">1</div>
<div class="abs step-label" style="left:386px">Lorem</div>
<div class="abs step-num" style="left:493px">2</div>
<div class="abs step-label" style="left:589px">Lorem</div>
<div class="abs step-num" style="left:694px">3</div>
<div class="abs step-label" style="left:789px">Lorem</div>
<div class="abs step-cta">Lorem ipsum</div>
<svg class="abs" style="left:355px;top:875px" width="345" height="50" viewBox="0 0 345 50" aria-hidden="true">
  <g fill="none" stroke="var(--grey-arrow)" stroke-width="6" stroke-linecap="round">
    <path d="M10 8 Q60 45 140 10"/><path d="M128 6 L142 8 L136 22"/>
    <path d="M214 14 Q260 50 330 14"/><path d="M318 8 L332 12 L324 26"/>
  </g>
</svg>

<div class="abs feature" style="left:160px"><h4>LOREM IPSUM</h4><p>Sed sem sapien, faucibus sit amet fermentum nec, dictum in felis. Donec dictum consequat</p></div>
<div class="abs feature" style="left:494px"><h4>LOREM IPSUM</h4><p>Sed sem sapien, faucibus sit amet fermentum nec, dictum in felis. Donec dictum consequat</p></div>
<div class="abs feature" style="left:794px"><h4>LOREM IPSUM</h4><p>Sed sem sapien, faucibus sit amet fermentum nec, dictum in felis. Donec dictum consequat</p></div>

<footer class="abs footer"><div class="footer-inner wood"></div></footer>
<div class="abs footer-links">LOREM IPSUM<span>|</span>LOREM IPSUM<span>|</span>LOREM IPSUM<span>|</span>LOREM IPSUM<span>|</span>LOREM IPSUM</div>
<div class="abs copyright">COPYRIGHT 2012 VURLEAF FRAME COMPANY</div>
<div class="abs social" style="left:916px;background:#3b5a9a"></div>
<div class="abs social" style="left:953px;background:#3fa9d9"></div>
<div class="abs social" style="left:991px;background:#e07a1f"></div>
<div class="abs social" style="left:1029px;background:#c8232c"></div>

</body>
</html>
```